Web Design Project - Event Management Company

A web-page design needs to be created for an event management company. The logo has already been created, the design needs to draw on the themes and colors of the logo and extend on that.

The event management company likes to differentiate itself from others by being a bit "un-conventional" and being able to think outside the box.

the specialise in corporate events, weddings, AGMs, anything that requires coordination of resources. They also can provide Audio Visual services such as recording events.

final design will also require HTML implementation

```html
<!DOCTYPE html>
<html lang="en">
<head>
<meta charset="utf-8">
<title>Odd Tile Group – Event Management</title>
<link href="https://fonts.googleapis.com/css2?family=Roboto+Condensed:wght@700&family=Josefin+Sans:wght@300&family=Open+Sans:wght@400&family=Oswald:wght@500&display=swap" rel="stylesheet">
<style>
  :root {
    --bg: #ffffff;
    --ink: #1b1b1b;
    --ink-soft: #3a3a3a;
    --brand-grey: #444444;
    --orange: #f3a03a;
    --pink: #f6b9cb;
    --blue: #5ec3e2;
    --red: #ee5a2b;
    --lime: #cfd51a;
    --rule: #d8d8d8;
    --link: #2a3ad6;
  }
  * { margin: 0; padding: 0; box-sizing: border-box; }
  html, body { width: 1200px; height: 1000px; overflow: hidden; background: var(--bg); }
  .page { position: relative; width: 1200px; height: 1000px; }

  .brand {
    position: absolute; left: 218px; top: 118px;
    display: flex; align-items: center; gap: 12px;
  }
  .brand-mark { width: 30px; height: 30px; background: var(--orange); }
  .brand-name {
    font-family: "Oswald", sans-serif; font-weight: 500;
    font-size: 34px; letter-spacing: 1px; color: var(--brand-grey);
    text-transform: uppercase;
  }

  .main-nav {
    position: absolute; top: 74px; right: 219px;
    display: flex; gap: 28px;
  }
  .main-nav a {
    font-family: "Roboto Condensed", sans-serif; font-weight: 700;
    font-size: 17px; color: var(--ink); text-decoration: none; letter-spacing: .3px;
  }

  .photo { position: absolute; }
  .photo--venue   { left: 308px; top: 214px; width: 165px; height: 147px; transform: rotate(-7deg); background: linear-gradient(160deg,#b23a4a,#6f8a4a 45%,#e9e9ea 70%); }
  .photo--crowd   { left: 518px; top: 222px; width: 163px; height: 140px; transform: rotate(4deg); background: linear-gradient(170deg,#7b4fa3,#2b1f3d 60%,#141018); }
  .photo--couple  { left: 724px; top: 200px; width: 155px; height: 134px; transform: rotate(1.5deg); background: linear-gradient(120deg,#3d5a2a,#b89a86 50%,#222 85%); }
  .photo--drinks  { left: 340px; top: 397px; width: 163px; height: 140px; transform: rotate(7deg); background: linear-gradient(150deg,#d8c8b4,#7a2a22 55%,#e0d2c0); }
  .photo--cake    { left: 517px; top: 415px; width: 153px; height: 135px; background: linear-gradient(180deg,#5f7a3a,#e9e4df 45%,#f0e8e6 80%,#e35a9a); }
  .photo--tables  { left: 683px; top: 380px; width: 168px; height: 143px; transform: rotate(-9deg); background: linear-gradient(160deg,#e8d8c8,#c9a6a0 50%,#7e1f24); }
  .photo--stage   { left: 355px; top: 580px; width: 153px; height: 133px; background: linear-gradient(150deg,#e9c89a,#b34a38 55%,#e3b47a); }
  .photo--banquet { left: 522px; top: 580px; width: 153px; height: 133px; background: linear-gradient(170deg,#5a2a12,#c26a2a 45%,#ece8e4 75%,#222); }
  .photo--catering{ left: 688px; top: 578px; width: 153px; height: 134px; background: linear-gradient(140deg,#e9e4dc,#b9b2a8 50%,#c87a3a); }

  .info-column { position: absolute; top: 757px; width: 192px; }
  .info-column--about    { left: 247px; }
  .info-column--services { left: 505px; }
  .info-column--clients  { left: 762px; }
  .info-title {
    display: flex; align-items: center; gap: 10px;
    font-family: "Josefin Sans", sans-serif; font-weight: 300;
    font-size: 29px; color: var(--ink-soft); line-height: 34px;
  }
  .info-title .tile { width: 21px; height: 21px; margin-top: -5px; }
  .info-column--about .tile    { background: var(--orange); }
  .info-column--services .tile { background: var(--pink); }
  .info-column--clients .tile  { background: var(--lime); }
  .info-text {
    margin-top: 10px;
    font-family: "Open Sans", sans-serif; font-size: 10.4px; line-height: 13.7px;
    color: var(--ink-soft); text-align: justify;
  }

  .column-divider { position: absolute; top: 782px; width: 1px; height: 104px; background: linear-gradient(var(--bg), var(--rule) 30%, var(--rule) 70%, var(--bg)); }
  .column-divider--one { left: 473px; }
  .column-divider--two { left: 731px; }

  .footer-stripe { position: absolute; left: 217px; top: 953px; width: 766px; display: flex; gap: 3px; }
  .footer-stripe span { flex: 1; height: 2px; }
  .footer-stripe .o { background: var(--orange); }
  .footer-stripe .p { background: var(--pink); }
  .footer-stripe .b { background: var(--blue); }
  .footer-stripe .r { background: var(--red); }
  .footer-stripe .l { background: var(--lime); }

  .copyright {
    position: absolute; top: 971px; left: 0; width: 1200px; text-align: center;
    font-family: "Open Sans", sans-serif; font-size: 10px; color: var(--ink-soft);
  }
  .copyright a { color: var(--link); text-decoration: none; }
</style>
</head>
<body>
<div class="page">
  <header>
    <div class="brand">
      <span class="brand-mark"></span>
      <span class="brand-name">Odd Tile Group</span>
    </div>
    <nav class="main-nav">
      <a href="#">HOME</a>
      <a href="#">ABOUT</a>
      <a href="#">SERVICES</a>
      <a href="#">GALLERY</a>
      <a href="#">CONTACT</a>
    </nav>
  </header>

  <section class="gallery">
    <div class="photo photo--venue" role="img" aria-label="Outdoor wedding venue with white chairs under a floral arch"></div>
    <div class="photo photo--crowd" role="img" aria-label="Conference audience seated in a purple-lit hall"></div>
    <div class="photo photo--couple" role="img" aria-label="Bride and groom smiling outdoors"></div>
    <div class="photo photo--drinks" role="img" aria-label="Waiters serving trays of wine glasses"></div>
    <div class="photo photo--cake" role="img" aria-label="Tiered white wedding cake with pink roses"></div>
    <div class="photo photo--tables" role="img" aria-label="Banquet tables set with flowers and glassware"></div>
    <div class="photo photo--stage" role="img" aria-label="Microphone in front of a lit event stage"></div>
    <div class="photo photo--banquet" role="img" aria-label="Candlelit reception hall with dressed chairs"></div>
    <div class="photo photo--catering" role="img" aria-label="Catering staff serving canapés"></div>
  </section>

  <section class="info">
    <article class="info-column info-column--about">
      <h2 class="info-title"><span class="tile"></span>ABOUT US</h2>
      <p class="info-text">Lorem Ipsum is simply dummy text of the printing and typesetting industry. Lorem Ipsum has been the industry's standard dummy text ever since the 1500s, when an unknown printer took a galley of type and scrambled it to make a type specimen book.ndustry's standard dummy text ever since the 1500s, when an unknown printer</p>
    </article>
    <div class="column-divider column-divider--one"></div>
    <article class="info-column info-column--services">
      <h2 class="info-title"><span class="tile"></span>SERVICES</h2>
      <p class="info-text">Lorem Ipsum is simply dummy text of the printing and typesetting industry. Lorem Ipsum has been the industry's standard dummy text ever since the 1500s, when an unknown printer took a galley of type and scrambled it to make a type specimen book.ndustry's standard dummy text ever since the 1500s, when an unknown printer</p>
    </article>
    <div class="column-divider column-divider--two"></div>
    <article class="info-column info-column--clients">
      <h2 class="info-title"><span class="tile"></span>CLIENTS</h2>
      <p class="info-text">Lorem Ipsum is simply dummy text of the printing and typesetting industry. Lorem Ipsum has been the industry's standard dummy text ever since the 1500s, when an unknown printer took a galley of type and scrambled it to make a type specimen book.ndustry's standard dummy text ever since the 1500s, when an unknown printer</p>
    </article>
  </section>

  <footer>
    <div class="footer-stripe">
      <span class="o"></span><span class="p"></span><span class="b"></span><span class="r"></span><span class="l"></span>
      <span class="o"></span><span class="p"></span><span class="b"></span><span class="r"></span><span class="l"></span>
    </div>
    <p class="copyright">Copyright © 2013 OddTileGroup. <a href="#">Privacy Policy</a></p>
  </footer>
</div>
</body>
</html>
```